Business Card Design

We offer full auto repair and auto customization from custom wheels to lift kits and drop kits we do it all. I want something that grabs your attention from the start but nothing flashy i am more of a clean crisp modern kinda of guy. I plan on using the design on my business cards and my main business sign .
Updates
I have up loaded an image of my currant business card designed by me , I would like to improve on it
Target Market(s)
20-35 male and female
Industry/Entity Type
Business
Contact Information for Business Card
Corvello Wheel Works
48362 Parkfield rd
Ashgrove OR, 97231
Manager: Dorian Walsh
P:555-214-7730
F:555-214-7781
Email:Dorian@corvellowheelandgarage.example
website:Corvellowheelandgarage.example
Look and feel

```html
<!DOCTYPE html>
<html lang="en">
<head>
<meta charset="utf-8">
<title>Corvello Wheel Works — Business Card</title>
<link rel="stylesheet" href="https://fonts.googleapis.com/css2?family=Open+Sans:wght@400;600;700&display=swap">
<style>
  :root {
    --red: #e52229;
    --black: #000000;
    --white: #ffffff;
    --ink: #1a1a1a;
    --backdrop: #2b2b2b;
    --card-w: 860px;
    --card-h: 492px;
  }
  * { box-sizing: border-box; margin: 0; padding: 0; }
  html, body {
    width: 1200px; height: 1200px; overflow: hidden;
    background: var(--backdrop);
    font-family: "Open Sans", Arial, sans-serif;
  }
  .sheet { position: relative; width: 1200px; height: 1200px; }
  .card {
    position: absolute; left: 170px;
    width: var(--card-w); height: var(--card-h);
    overflow: hidden;
    box-shadow: 0 10px 30px rgba(0,0,0,.45);
  }
  .band { position: absolute; background: var(--red); }
  ul { list-style: none; }

  /* Front */
  .card-front { top: 78px; background: var(--black); }
  .card-front .band-top { left: 36px; right: 36px; top: 20px; height: 42px; }
  .card-front .band-bottom { left: 36px; right: 36px; bottom: 22px; height: 46px; }
  .front-brand {
    position: absolute; left: 0; right: 0; top: 186px;
    display: flex; align-items: center; justify-content: center; gap: 18px;
    color: var(--red); font-weight: 600; font-size: 52px; letter-spacing: 1px;
  }
  .brand-dot { width: 26px; height: 26px; border-radius: 50%; background: var(--red); flex: none; }
  .services {
    position: absolute; left: 60px; right: 60px; bottom: 84px;
    display: flex; justify-content: space-between;
    color: var(--white); font-size: 17px; font-weight: 600; letter-spacing: .5px;
    text-transform: uppercase;
  }

  /* Back */
  .card-back { top: 630px; background: var(--white); }
  .card-back .band-top { left: 180px; right: 26px; top: 0; height: 36px; }
  .card-back .band-bottom { left: 0; right: 70px; bottom: 18px; height: 40px; }
  .back-brand {
    position: absolute; left: 34px; top: 54px;
    display: flex; align-items: center; gap: 12px;
    color: var(--red); font-weight: 600; font-size: 30px;
  }
  .back-brand .brand-dot { width: 16px; height: 16px; }
  .person { position: absolute; left: 34px; top: 132px; }
  .person-name { color: var(--red); font-weight: 700; font-size: 30px; letter-spacing: .5px; text-transform: uppercase; }
  .person-role { color: var(--ink); font-size: 19px; font-weight: 600; margin-top: 2px; }
  .rule { position: absolute; left: 34px; top: 228px; width: 440px; height: 3px; background: var(--red); }
  .contacts { position: absolute; left: 34px; top: 246px; }
  .contacts li {
    display: flex; align-items: center; gap: 10px;
    color: var(--ink); font-size: 17px; font-weight: 600; line-height: 30px;
  }
  .contacts svg { width: 16px; height: 16px; fill: var(--red); flex: none; }
  .brands { position: absolute; right: 30px; top: 58px; text-align: right; }
  .brands-title { color: var(--ink); font-size: 14px; font-weight: 600; text-transform: uppercase; letter-spacing: .4px; margin-bottom: 14px; }
  .brand-list li {
    display: flex; align-items: center; justify-content: flex-end; gap: 8px;
    color: var(--ink); font-size: 15px; font-weight: 600; line-height: 22px; text-transform: uppercase;
  }
  .brand-list li::after {
    content: ""; width: 12px; height: 12px; border-radius: 50%;
    background: var(--red); border: 2px solid #7a0d10; flex: none;
  }
  .brands-more { color: var(--ink); font-size: 15px; font-weight: 600; text-transform: uppercase; margin-top: 10px; padding-right: 20px; }
</style>
</head>
<body>
<main class="sheet">

  <section class="card card-front" aria-label="Business card front">
    <div class="band band-top"></div>
    <div class="front-brand"><span class="brand-dot"></span>Corvello Wheel Works</div>
    <ul class="services">
      <li>New and used tires</li>
      <li>Custom wheels</li>
      <li>Tire repair</li>
      <li>Shocks</li>
      <li>Brakes</li>
    </ul>
    <div class="band band-bottom"></div>
  </section>

  <section class="card card-back" aria-label="Business card back">
    <div class="band band-top"></div>
    <div class="back-brand"><span class="brand-dot"></span>Corvello Wheel Works</div>

    <div class="person">
      <p class="person-name">Dorian Walsh</p>
      <p class="person-role">Manager</p>
    </div>
    <div class="rule"></div>

    <ul class="contacts">
      <li><svg viewBox="0 0 24 24" aria-hidden="true"><path d="M6.6 10.8a15 15 0 0 0 6.6 6.6l2.2-2.2a1 1 0 0 1 1-.25 11.4 11.4 0 0 0 3.6.57 1 1 0 0 1 1 1V20a1 1 0 0 1-1 1A17 17 0 0 1 3 4a1 1 0 0 1 1-1h3.5a1 1 0 0 1 1 1c0 1.25.2 2.45.57 3.57a1 1 0 0 1-.25 1z"/></svg>555-214-7730</li>
      <li><svg viewBox="0 0 24 24" aria-hidden="true"><path d="M6 2h12v6H6zM4 9h16a2 2 0 0 1 2 2v6h-4v5H6v-5H2v-6a2 2 0 0 1 2-2zm4 8v3h8v-3z"/></svg>555-214-7781</li>
      <li><svg viewBox="0 0 24 24" aria-hidden="true"><path d="M2 5h20v14H2zm2 2v.5l8 5 8-5V7z"/></svg>Dorian@corvellowheelandgarage.example</li>
      <li><svg viewBox="0 0 24 24" aria-hidden="true"><path d="M10 3a7 7 0 0 1 5.6 11.2l5.6 5.6-1.4 1.4-5.6-5.6A7 7 0 1 1 10 3zm0 2a5 5 0 1 0 0 10 5 5 0 0 0 0-10z"/></svg>Corvellowheelandgarage.example</li>
      <li><svg viewBox="0 0 24 24" aria-hidden="true"><path d="M12 3l10 9h-3v9h-5v-6h-4v6H5v-9H2z"/></svg>48362 Parkfield rd Ashgrove OR, 97231</li>
    </ul>

    <div class="brands">
      <p class="brands-title">We carry the industries finest</p>
      <ul class="brand-list">
        <li>Larkmont Forge</li>
        <li>Halvern Racing</li>
        <li>KVR</li>
        <li>DZL</li>
        <li>TRQ</li>
        <li>Ostrel GT Series</li>
        <li>Vantor Metal</li>
        <li>Brisk Fuel</li>
        <li>Kesso</li>
        <li>Ravi</li>
        <li>BT Hollister</li>
        <li>Arlemont</li>
      </ul>
      <p class="brands-more">And many more</p>
    </div>

    <div class="band band-bottom"></div>
  </section>

</main>
</body>
</html>
```